New Poster Design for Film Festival

Hi! We need a poster design for our student film festival and the Thornfield State University. We screen over 300 short films over a 3 days in May. Our committee wants a look feel similar to the image we attached below.

Target Market(s)

Students and general audience.

Industry/Entity Type

Festival

Colors
3377b5
85abd2
34b8a4
f68e4e

Requirements
Must have
• Larkspur Film Festival
17th Annual
May 2-3-4 2014
Ada Penhallow Theatre
Free Admission
Department of Screen and Digital Storytelling

Poster size 36" (high) x 24" (wide)
Thornfield State University
www.larkspurfilmfest.example
Nice to have
• Bold lettering
Should not have
• Flamingos - hate them :)

```html
<!DOCTYPE html>
<html lang="en">
<head>
<meta charset="utf-8">
<title>Larkspur Film Festival – 17th Annual Poster</title>
<link rel="stylesheet" href="https://fonts.googleapis.com/css2?family=Oswald:wght@500;700&family=Roboto+Condensed:wght@500;700&family=Arimo:wght@700&display=swap">
<style>
  :root {
    --backdrop: #f3f3f3;
    --teal: #34b8a4;
    --teal-deep: #2a9d89;
    --teal-glow: #e4f5f2;
    --orange: #f68e4e;
    --white: #ffffff;
  }
  * { margin: 0; padding: 0; box-sizing: border-box; }
  html, body {
    width: 1200px; height: 1000px; overflow: hidden;
    background: radial-gradient(ellipse at center, #ffffff 0%, var(--backdrop) 70%, #e8e8e8 100%);
  }
  .poster {
    position: absolute; left: 277px; top: 13px;
    width: 640px; height: 962px;
  }
  .poster-head {
    position: absolute; left: 0; top: 0; width: 640px; height: 392px;
    background: radial-gradient(ellipse 55% 60% at 50% 100%, var(--teal-glow) 0%, #7fd0c3 35%, var(--teal) 80%);
  }
  .title-block {
    position: absolute; left: 106px; top: 0; width: 426px; height: 368px;
    background: var(--teal-deep);
    display: flex; flex-direction: column; align-items: center; justify-content: center;
    color: var(--white);
    font-family: "Oswald", "Arial Narrow", sans-serif; font-weight: 500;
    text-transform: uppercase; line-height: 1;
  }
  .title-block .title-name { font-size: 62px; letter-spacing: 10px; margin-right: -10px; }
  .title-block .title-film { font-size: 120px; font-weight: 700; letter-spacing: 14px; margin: 8px -14px 10px 0; }
  .title-block .title-festival { font-size: 62px; letter-spacing: 10px; margin-right: -10px; }
  .anniversary-band {
    position: absolute; left: 0; top: 392px; width: 640px; height: 336px;
    background: var(--white);
    display: flex; align-items: center; justify-content: center; gap: 26px;
  }
  .ordinal {
    font-family: "Oswald", "Arial Narrow", sans-serif; font-weight: 700;
    color: var(--orange); line-height: 1;
    display: flex; align-items: flex-start;
  }
  .ordinal .ordinal-number { font-size: 290px; letter-spacing: -4px; }
  .ordinal .ordinal-suffix { font-size: 96px; margin-top: 38px; margin-left: 6px; }
  .annual {
    font-family: "Oswald", "Arial Narrow", sans-serif; font-weight: 700;
    font-size: 54px; letter-spacing: 8px; line-height: 1;
    color: var(--orange);
    writing-mode: vertical-rl; transform: rotate(180deg);
  }
  .poster-foot {
    position: absolute; left: 0; top: 728px; width: 640px; height: 234px;
    background: radial-gradient(ellipse 55% 65% at 50% 0%, #a6e0d6 0%, #6fcbbb 40%, var(--teal) 85%);
    color: var(--white);
  }
  .event-details, .organiser {
    position: absolute; top: 38px;
    font-family: "Roboto Condensed", "Arial Narrow", sans-serif; font-weight: 500;
    font-size: 26px; line-height: 33px;
  }
  .event-details { left: 24px; }
  .organiser { right: 20px; text-align: right; }
  .festival-url {
    position: absolute; left: 0; width: 100%; top: 168px; text-align: center;
    font-family: "Arimo", Arial, sans-serif; font-weight: 700; font-size: 24px; letter-spacing: 0.3px;
  }
</style>
</head>
<body>
  <main class="poster">
    <section class="poster-head">
      <h1 class="title-block">
        <span class="title-name">Larkspur</span>
        <span class="title-film">Film</span>
        <span class="title-festival">Festival</span>
      </h1>
    </section>

    <section class="anniversary-band">
      <p class="ordinal"><span class="ordinal-number">17</span><span class="ordinal-suffix">th</span></p>
      <p class="annual">ANNUAL</p>
    </section>

    <section class="poster-foot">
      <p class="event-details">May 2-3-4 2014<br>Ada Penhallow Theatre<br>FREE ADMISSION</p>
      <p class="organiser">Department of Screen and<br>Digital Storytelling<br>Thornfield State University</p>
      <p class="festival-url">www.larkspurfilmfest.example</p>
    </section>
  </main>
</body>
</html>
```